Sunder Grove

using the same elements in this label (size 4L x 2W). the package will hold a 3ml syringe in a rectangular plastic pouch. label will go on the pouch this is a marijuana product, made for pain relief. We will need indica and hybrid indications on label. the 3 monkeys are see no evil
,hear no evil, say no evil. the CA/marijuana symbol must be used. u can use other colors and font/fonts.

```html
<!DOCTYPE html>
<html lang="en">
<head>
<meta charset="utf-8">
<title>Sunder Grove RSO Syringe Label</title>
<link rel="stylesheet" href="https://fonts.googleapis.com/css2?family=Lato:wght@700;900&display=swap">
<style>
  :root {
    --page: #ffffff;
    --night: #1a191c;
    --ember: #8a1f22;
    --violet: #3a2d8a;
    --maroon: #5c1a1a;
    --maroon-light: #6e2020;
    --gold: #e2b646;
    --white: #ffffff;
    --oil-dark: #4a3b16;
    --oil-light: #9a8446;
    --fur-dark: #6b4424;
    --fur-light: #c99a6a;
  }
  * { margin: 0; padding: 0; box-sizing: border-box; }
  html, body {
    width: 1200px;
    height: 715px;
    overflow: hidden;
    background: var(--page);
    font-family: "Lato", Arial, sans-serif;
  }
  .label {
    position: absolute;
    left: 120px;
    top: 118px;
    width: 960px;
    height: 478px;
    overflow: hidden;
    background:
      radial-gradient(ellipse 420px 260px at 0% 40%, rgba(138,31,34,0.75), transparent 70%),
      radial-gradient(ellipse 460px 300px at 100% 0%, rgba(58,45,138,0.85), transparent 70%),
      var(--night);
  }
  .label__wave {
    position: absolute;
    inset: 0;
    width: 100%;
    height: 100%;
  }
  .brand-name {
    position: absolute;
    left: 68px;
    top: 52px;
    font-weight: 900;
    font-size: 68px;
    line-height: 1;
    color: var(--white);
    letter-spacing: 1px;
  }
  .product-name {
    position: absolute;
    left: 96px;
    top: 152px;
    font-weight: 900;
    font-size: 64px;
    line-height: 1;
    color: var(--gold);
    letter-spacing: 0.5px;
  }
  .strain-type {
    position: absolute;
    right: 36px;
    top: 36px;
    font-weight: 700;
    font-size: 33px;
    line-height: 1;
    color: var(--gold);
  }
  .syringe-art {
    position: absolute;
    left: 54px;
    top: 250px;
    width: 466px;
    height: 184px;
    border-radius: 40px;
    background: linear-gradient(160deg, transparent 0%, rgba(200,205,210,0.35) 30%, var(--oil-light) 55%, var(--oil-dark) 100%);
  }
  .monkeys-art {
    position: absolute;
    left: 550px;
    top: 129px;
    width: 388px;
    height: 250px;
    border-radius: 60px 60px 20px 20px;
    background: radial-gradient(ellipse at 50% 45%, var(--fur-light), var(--fur-dark) 80%);
  }
  .net-weight {
    position: absolute;
    left: 518px;
    top: 408px;
    font-weight: 700;
    font-size: 33px;
    line-height: 1;
    color: var(--white);
  }
  .compliance-badge {
    position: absolute;
    top: 399px;
    width: 53px;
    height: 53px;
    border: 3px solid var(--white);
    border-radius: 8px;
  }
  .compliance-badge--state { left: 806px; }
  .compliance-badge--warning { left: 879px; }
</style>
</head>
<body>
  <main class="label">
    <svg class="label__wave" viewBox="0 0 960 478" preserveAspectRatio="none" aria-hidden="true">
      <path d="M0 120 C 60 300, 200 380, 380 392 C 560 404, 700 340, 960 312 L960 478 L0 478 Z" fill="var(--maroon-light)"/>
      <path d="M0 170 C 80 330, 220 400, 400 400 C 580 400, 720 350, 960 322 L960 478 L0 478 Z" fill="var(--maroon)"/>
    </svg>

    <h1 class="brand-name">Sunder Grove</h1>
    <h2 class="product-name">RSO SYRINGE</h2>
    <p class="strain-type">Indica | Hybrid</p>

    <div class="syringe-art" role="img" aria-label="Illustration of a glass oral syringe filled with amber cannabis oil"></div>
    <div class="monkeys-art" role="img" aria-label="Illustration of three seated monkeys: see no evil, hear no evil, speak no evil"></div>

    <p class="net-weight">1 GRAM (.035oz)</p>
    <div class="compliance-badge compliance-badge--state" role="img" aria-label="State cannabis symbol"></div>
    <div class="compliance-badge compliance-badge--warning" role="img" aria-label="Product warning symbol"></div>
  </main>
</body>
</html>
```